Animated Graphics for Article-Author Connection App

An Zoka for editor and writers. We want to show screens for a app that connects editor that need articles written and authors who want to write them. But a car/map analogy doesn't work. How about a sun and planet analogy. This can be done withe the following screens:

Screen 1. icons of various industries (aviation, architecture, manufacturing, etc.)

Screen 2. one industry (aviation, shown with a plane icon) shoots out an idea (use light bulb icon) to writers, who appear in an arc around the airplane. Like planets in stationary orbit. When the idea nears the arc, the writer rotates in the orbit to accept it and glows.
Screen 3. writer shoots out article to tech editor
Screen 4. tech editor shoots out article to copy editors
Screen 5. copy editor shoots out article to production person

Target Market(s)

Engineers, editors, authors

Industry/Entity Type

Mechanical Engineering

Colors
dbdbdb
aaaaaa
000000
33a6d7
85acd3
3276b5

Requirements
Must have
• Simple and attractive. Color scheme like Zoka.
Nice to have
• The article or idea have a flag on which 3 pieces of information are shown
• 1) due date
• 2) length
• 3)price

```html
<!DOCTYPE html>
<html lang="en">
<head>
<meta charset="utf-8">
<title>Industry Orbit Screen</title>
<link href="https://fonts.googleapis.com/css2?family=Oswald:wght@300;400&display=swap" rel="stylesheet">
<style>
  :root{
    --bar-dark:#1f1f1f;
    --bar-light:#2e2e2e;
    --panel:#1b1b1b;
    --panel-line:#2c2c2c;
    --stage:#ffffff;
    --orbit:#dbdbdb;
    --ring-grey:#aaaaaa;
    --sun-blue:#33a6d7;
    --light-blue:#85acd3;
    --deep-blue:#3276b5;
    --band-pink:#fbdde1;
    --band-text:#ffffff;
    --red:#e8141c;
    --green:#8cc63f;
    --black:#000000;
    --icon:#d9d9d9;
  }
  *{margin:0;padding:0;box-sizing:border-box}
  html,body{width:779px;height:1200px;overflow:hidden;background:var(--stage)}
  .app{position:relative;width:779px;height:1200px;overflow:hidden;font-family:'Oswald',sans-serif}
  .top-bar{position:absolute;left:0;top:0;width:779px;height:125px;background:linear-gradient(var(--bar-light),var(--bar-dark))}
  .search-key{position:absolute;right:95px;top:52px;color:var(--icon);font-size:30px;font-weight:300;line-height:1}
  .stage{position:absolute;left:0;top:125px;width:779px;height:646px;background:var(--stage);overflow:hidden}
  .industry-band{position:absolute;left:0;top:30px;width:370px;height:105px;background:var(--band-pink)}
  .industry-name{position:absolute;left:88px;top:30px;color:var(--band-text);font-size:38px;font-weight:400;letter-spacing:3px;line-height:1.1}
  .bottom-panel{position:absolute;left:0;top:771px;width:779px;height:429px;background:var(--panel)}
  .divider{position:absolute;top:0;width:2px;height:429px;background:var(--panel-line)}
  svg{position:absolute;left:0;top:0}
</style>
</head>
<body>
<div class="app">
  <header class="top-bar">
    <svg class="menu-icon" width="140" height="125" viewBox="0 0 140 125">
      <polygon points="42,50 88,50 96,58 42,58" fill="var(--icon)"/>
      <polygon points="42,64 100,64 108,72 42,72" fill="var(--icon)"/>
      <polygon points="42,78 112,78 120,86 42,86" fill="var(--icon)"/>
    </svg>
    <span class="search-key">Q</span>
  </header>

  <main class="stage">
    <div class="industry-band">
      <span class="industry-name">AVIATION</span>
      <svg class="plane-icon" width="370" height="105" viewBox="0 0 370 105">
        <g fill="#ffffff">
          <rect x="290" y="48" width="54" height="9" rx="4"/>
          <polygon points="312,50 324,50 314,22 306,22"/>
          <polygon points="312,55 324,55 314,83 306,83"/>
          <polygon points="290,50 296,50 290,38 285,38"/>
          <polygon points="290,55 296,55 290,67 285,67"/>
        </g>
      </svg>
    </div>

    <svg class="orbit-scene" width="779" height="646" viewBox="0 125 779 646">
      <path d="M416 205 Q660 250 702 560" fill="none" stroke="var(--orbit)" stroke-width="6"/>
      <g fill="var(--orbit)">
        <circle cx="416" cy="205" r="9"/>
        <circle cx="530" cy="230" r="9"/>
        <circle cx="612" cy="290" r="9"/>
        <circle cx="665" cy="375" r="9"/>
      </g>

      <g class="writers" fill="#ffffff" stroke="var(--sun-blue)">
        <circle cx="546" cy="416" r="30" stroke-width="8" stroke="var(--light-blue)"/>
        <circle cx="578" cy="448" r="34" stroke-width="8" stroke="var(--light-blue)"/>
        <circle cx="617" cy="482" r="38" stroke-width="8"/>
        <circle cx="660" cy="520" r="42" stroke-width="8"/>
      </g>
      <circle class="active-writer" cx="702" cy="577" r="58" fill="#ffffff" stroke="var(--orbit)" stroke-width="3"/>

      <defs>
        <radialGradient id="sunRing" cx="50%" cy="50%" r="50%">
          <stop offset="88%" stop-color="#1a1a1a"/>
          <stop offset="96%" stop-color="#777777"/>
          <stop offset="100%" stop-color="#dddddd"/>
        </radialGradient>
      </defs>
      <circle class="sun-ring" cx="403" cy="770" r="222" fill="url(#sunRing)"/>
      <circle class="sun-edge" cx="403" cy="770" r="206" fill="#ffffff"/>
      <circle class="sun" cx="403" cy="770" r="198" fill="var(--sun-blue)"/>
      <rect x="386" y="762" width="34" height="10" rx="2" fill="#8a8a8a"/>

      <g class="industry-switches">
        <rect x="28" y="150" width="36" height="460" fill="#c9c9c9"/>
        <g fill="#9a9a9a">
          <rect x="24" y="160" width="44" height="6"/><rect x="24" y="256" width="44" height="6"/>
          <rect x="24" y="268" width="44" height="6"/><rect x="24" y="362" width="44" height="6"/>
          <rect x="24" y="374" width="44" height="6"/><rect x="24" y="462" width="44" height="6"/>
          <rect x="24" y="474" width="44" height="6"/><rect x="24" y="572" width="44" height="6"/>
          <rect x="24" y="584" width="44" height="6"/><rect x="24" y="596" width="44" height="6"/>
        </g>
        <rect x="14" y="178" width="60" height="60" rx="8" fill="#222"/>
        <rect x="20" y="184" width="48" height="48" rx="6" fill="var(--red)"/>
        <rect x="14" y="285" width="60" height="60" rx="8" fill="#222"/>
        <rect x="20" y="291" width="48" height="48" rx="6" fill="var(--green)"/>
        <rect x="14" y="388" width="60" height="60" rx="8" fill="#222"/>
        <rect x="20" y="394" width="48" height="48" rx="6" fill="var(--deep-blue)"/>
        <rect x="0" y="478" width="74" height="82" rx="8" fill="var(--black)"/>
        <rect x="20" y="496" width="48" height="48" rx="6" fill="var(--black)" stroke="#555" stroke-width="3"/>
      </g>
    </svg>
  </main>

  <footer class="bottom-panel">
    <div class="divider" style="left:91px"></div>
    <div class="divider" style="left:390px"></div>
    <div class="divider" style="left:681px"></div>
    <svg class="tool-icons" width="779" height="429" viewBox="0 0 779 429">
      <g fill="none" stroke="var(--icon)" stroke-width="3">
        <rect x="710" y="30" width="36" height="40" rx="3"/>
        <line x1="710" y1="40" x2="746" y2="40"/>
        <rect x="710" y="135" width="38" height="38" rx="4"/>
        <rect x="716" y="129" width="38" height="38" rx="4"/>
        <rect x="710" y="238" width="38" height="40" rx="3"/>
        <line x1="720" y1="238" x2="720" y2="278"/>
      </g>
      <text x="728" y="63" fill="var(--icon)" font-family="Oswald, sans-serif" font-size="16" text-anchor="middle">19</text>
    </svg>
  </footer>
</div>
</body>
</html>
```